Looking for a clean, modern, and professional business card design that reflects Valtrim Systems

The design should include the company logo, contact details, and align with our brand identity. Please use a sophisticated and minimalist style, incorporating [specific colors, if applicable]. Creativity is welcome, but the card must maintain a polished and professional appearance.

Details to Include:

Name: Gavin Trelowe
Title: VP Sales / Operations
Company: Valtrim Systems
Phone: 483.216.7705
Email: gavin@valtrimsystems-example.com
Website: www.valtrimsystems-example.com

```html
<!DOCTYPE html>
<html lang="en">
<head>
<meta charset="utf-8">
<title>Valtrim Systems — Business Card</title>
<link rel="stylesheet" href="https://fonts.googleapis.com/css2?family=Montserrat:wght@500;600;700&family=Open+Sans:wght@400;600&display=swap">
<style>
  :root {
    --brand-blue: #3470b2;
    --brand-blue-light: #cfe4f7;
    --ink: #111418;
    --paper: #ffffff;
    --backdrop: #e9ebee;
  }
  html, body {
    margin: 0;
    padding: 0;
    width: 1200px;
    height: 874px;
    overflow: hidden;
    background: var(--backdrop);
  }
  .canvas {
    position: relative;
    width: 1200px;
    height: 874px;
  }
  .card {
    position: absolute;
    left: 280px;
    width: 640px;
    height: 366px;
    border-radius: 22px;
    overflow: hidden;
    background: var(--brand-blue);
    box-shadow: 0 6px 18px rgba(0,0,0,0.15);
  }
  .card--front { top: 48px; }
  .card--back { top: 460px; }

  .wordmark {
    font-family: "Montserrat", sans-serif;
    font-weight: 700;
    letter-spacing: 0.06em;
    text-transform: uppercase;
    white-space: nowrap;
  }
  .card--front .wordmark {
    position: absolute;
    left: 0; right: 0;
    top: 138px;
    text-align: center;
    font-size: 44px;
    color: var(--brand-blue-light);
  }
  .card--front .website {
    position: absolute;
    left: 0; right: 0;
    bottom: 42px;
    text-align: center;
    font-family: "Open Sans", sans-serif;
    font-size: 14px;
    color: var(--paper);
  }

  .panel-shape {
    position: absolute;
    inset: 0;
  }
  .card--back .wordmark {
    position: absolute;
    left: 300px;
    width: 320px;
    top: 168px;
    text-align: center;
    font-size: 28px;
    color: var(--ink);
  }
  .identity {
    position: absolute;
    left: 32px;
    top: 34px;
    color: var(--paper);
  }
  .identity .name {
    font-family: "Montserrat", sans-serif;
    font-weight: 700;
    font-size: 22px;
    margin: 0;
  }
  .identity .title {
    font-family: "Open Sans", sans-serif;
    font-size: 13px;
    margin: 2px 0 0;
  }
  .contacts {
    position: absolute;
    left: 32px;
    bottom: 48px;
    margin: 0;
    padding: 0;
    list-style: none;
    font-family: "Open Sans", sans-serif;
    font-size: 12px;
    color: var(--paper);
  }
  .contacts li {
    display: flex;
    align-items: center;
    gap: 8px;
    line-height: 21px;
    white-space: nowrap;
  }
  .contacts svg {
    width: 11px;
    height: 11px;
    fill: var(--paper);
    flex: none;
  }
</style>
</head>
<body>
<main class="canvas">
  <section class="card card--front" aria-label="Card front">
    <div class="wordmark">Valtrim Systems</div>
    <div class="website">www.valtrimsystems-example.com</div>
  </section>

  <section class="card card--back" aria-label="Card back">
    <svg class="panel-shape" viewBox="0 0 640 366" width="640" height="366" aria-hidden="true">
      <polygon points="412,0 640,0 640,366 318,366 266,172" fill="var(--paper)"/>
      <polyline points="416,4 278,172 328,366" fill="none" stroke="var(--ink)" stroke-width="5"/>
    </svg>

    <div class="identity">
      <p class="name">Gavin Trelowe</p>
      <p class="title">VP Sales / Operations</p>
    </div>

    <ul class="contacts">
      <li>
        <svg viewBox="0 0 24 24" aria-hidden="true"><path d="M6.6 10.8a15 15 0 0 0 6.6 6.6l2.2-2.2c.3-.3.7-.4 1-.2 1.1.4 2.3.6 3.6.6.6 0 1 .4 1 1V20c0 .6-.4 1-1 1A17 17 0 0 1 3 4c0-.6.4-1 1-1h3.5c.6 0 1 .4 1 1 0 1.3.2 2.5.6 3.6.1.3 0 .7-.2 1z"/></svg>
        483.216.7705
      </li>
      <li>
        <svg viewBox="0 0 24 24" aria-hidden="true"><path d="M2 5h20v14H2zm2 2v.5l8 5 8-5V7l-8 5z"/></svg>
        gavin@valtrimsystems-example.com
      </li>
      <li>
        <svg viewBox="0 0 24 24" aria-hidden="true"><path d="M12 2a10 10 0 1 0 0 20 10 10 0 0 0 0-20zm-1 17.9A8 8 0 0 1 4.1 11H7c.1 3 1.5 6.2 4 8.9zM4.1 9A8 8 0 0 1 11 4.1C9 6.3 7.3 8 7 9zm8.9 10.9c2.5-2.7 3.9-5.9 4-8.9h2.9a8 8 0 0 1-6.9 8.9zM17 9c-.3-1-2-2.7-4-4.9A8 8 0 0 1 19.9 9zm-8 2h6c-.1 2.6-1.2 5.2-3 7.3-1.8-2.1-2.9-4.7-3-7.3zm0-2c.3-1.4 1.3-3.1 3-5 1.7 1.9 2.7 3.6 3 5z"/></svg>
        www.valtrimsystems-example.com
      </li>
    </ul>

    <div class="wordmark">Valtrim Systems</div>
  </section>
</main>
</body>
</html>
```